Professional/modern business card design for construction company

We need a new business card design, double sided keeping it modern, sleek, professional and simple. We are an earthmoving business but do not want any pictures of machinery. I would like one side to have the logo and the other to have all the information, keeping with the colors in our logo. The business card will need to be able to be customised so we can use it for several different managers., we would also like to be able to use the design to apply it to other stationary ie. letterheads, notebooks etc. We do not really have a tag line but we could put on there that we specialise in - Agriculture, Civil Construction and Mining.

Contact Information for Business Card

Brolga Ridge Excavations Pty Ltd
ABN 58 402 937 615
82 Gumleaf Creek Road, Moree NSW 2400

Harold Benton
Managing Director
P 0418 639 204
E haroldbenton@brolgaridgeexc.com.au

Font styles to use
Serif
Sans Serif

Requirements
Nice to have
• I have attached some examples of ideas.
Should not have
• images of machinery

```html
<!DOCTYPE html>
<html lang="en">
<head>
<meta charset="utf-8">
<title>Brolga Ridge Excavations – Business Card</title>
<link rel="stylesheet" href="https://fonts.googleapis.com/css2?family=Montserrat:wght@400;500;700&family=Crimson+Pro:wght@500&display=swap">
<style>
  :root {
    --orange: #f58a1f;
    --charcoal: #424242;
    --ink: #3a3a3a;
    --role-ink: #4a3a2a;
    --paper: #f7f7f7;
    --white: #ffffff;
    --edge: #d8d8d8;
  }
  * { box-sizing: border-box; margin: 0; padding: 0; }
  html, body { width: 1200px; height: 900px; overflow: hidden; background: var(--white); }
  body { position: relative; font-family: "Montserrat", Arial, sans-serif; color: var(--ink); }

  .card { position: absolute; left: 278px; width: 643px; height: 367px; }
  .card--front { top: 52px; background: var(--paper); border: 1px solid var(--edge); }
  .card--back { top: 478px; background: var(--charcoal); }

  .brand { position: absolute; display: flex; align-items: center; gap: 10px; }
  .brand__mark { width: 14px; height: 14px; background: var(--orange); flex: none; }
  .brand__name { font-weight: 700; font-size: 15px; line-height: 1.25; letter-spacing: 0.5px; text-transform: uppercase; white-space: nowrap; }
  .brand__line { display: block; }
  .card--front .brand { left: 48px; top: 140px; }
  .card--front .brand__name { color: var(--ink); }
  .card--back .brand { left: 50%; top: 50%; transform: translate(-50%, -50%); }
  .card--back .brand__name { color: var(--white); font-size: 18px; }

  .company-details { position: absolute; left: 22px; top: 206px; list-style: none; }
  .company-details li { display: flex; align-items: center; gap: 9px; height: 22px; font-size: 11px; letter-spacing: 0.2px; white-space: nowrap; }
  .icon { width: 16px; height: 16px; flex: none; }

  .person-panel {
    position: absolute; left: 323px; top: 84px; width: 308px; height: 201px;
    background: var(--white); box-shadow: 0 6px 16px rgba(0,0,0,0.14);
  }
  .person-panel__lines { position: absolute; left: 0; top: 0; }
  .name-plate {
    position: absolute; left: 46px; top: 42px; width: 211px; height: 51px;
    background: var(--orange); color: var(--white); text-align: center; padding-top: 6px;
  }
  .name-plate__name { font-family: "Crimson Pro", Georgia, serif; font-weight: 500; font-size: 19px; letter-spacing: 1px; text-transform: uppercase; }
  .name-plate__role { font-size: 11px; letter-spacing: 0.6px; text-transform: uppercase; color: var(--role-ink); margin-top: 1px; }
  .contact { position: absolute; left: 46px; display: flex; align-items: center; gap: 6px; font-size: 11px; letter-spacing: 0; white-space: nowrap; }
  .contact--phone { top: 133px; }
  .contact--email { top: 155px; }
  .icon--boxed { width: 15px; height: 15px; }
</style>
</head>
<body>

<section class="card card--front">
  <div class="brand">
    <span class="brand__mark"></span>
    <span class="brand__name"><span class="brand__line">Brolga Ridge</span><span class="brand__line">Excavations Pty Ltd</span></span>
  </div>

  <ul class="company-details">
    <li>
      <svg class="icon" viewBox="0 0 16 16"><rect x="0.5" y="0.5" width="15" height="15" fill="none" stroke="var(--orange)"/><text x="8" y="10" font-size="4.5" text-anchor="middle" fill="var(--orange)" font-family="Arial, sans-serif">ABN</text></svg>
      <span>58 402 937 615</span>
    </li>
    <li>
      <svg class="icon" viewBox="0 0 16 16"><rect x="0.5" y="0.5" width="15" height="15" fill="none" stroke="var(--orange)"/><path d="M8 12.5 C6 10 5 8.5 5 7 a3 3 0 0 1 6 0 c0 1.5-1 3-3 5.5z" fill="none" stroke="var(--orange)"/><circle cx="8" cy="7" r="1" fill="var(--orange)"/></svg>
      <span>82 Gumleaf Creek Road, Moree NSW 2400</span>
    </li>
  </ul>

  <div class="person-panel">
    <svg class="person-panel__lines" width="60" height="170" viewBox="0 0 60 170">
      <path d="M46 57 H29 V140 H46" fill="none" stroke="var(--orange)"/>
      <path d="M46 79 H23 V162 H46" fill="none" stroke="var(--orange)"/>
    </svg>
    <div class="name-plate">
      <div class="name-plate__name">Harold Benton</div>
      <div class="name-plate__role">Managing Director</div>
    </div>
    <div class="contact contact--phone">
      <svg class="icon icon--boxed" viewBox="0 0 16 16"><rect x="0.5" y="0.5" width="15" height="15" fill="none" stroke="var(--orange)"/><path d="M5 4 l2 0 l0.8 2.2 l-1.2 0.9 a6 6 0 0 0 2.3 2.3 l0.9-1.2 l2.2 0.8 l0 2 a1 1 0 0 1-1 1 a8 8 0 0 1-7-7 a1 1 0 0 1 1-1z" fill="var(--orange)"/></svg>
      <span>0418 639 204</span>
    </div>
    <div class="contact contact--email">
      <svg class="icon icon--boxed" viewBox="0 0 16 16"><rect x="0.5" y="0.5" width="15" height="15" fill="none" stroke="var(--orange)"/><rect x="4" y="5" width="8" height="6" fill="var(--orange)"/><path d="M4 5 L8 8.5 L12 5" fill="none" stroke="var(--white)" stroke-width="0.8"/></svg>
      <span>haroldbenton@brolgaridgeexc.com.au</span>
    </div>
  </div>
</section>

<section class="card card--back">
  <div class="brand">
    <span class="brand__mark"></span>
    <span class="brand__name"><span class="brand__line">Brolga Ridge</span><span class="brand__line">Excavations Pty Ltd</span></span>
  </div>
</section>

</body>
</html>
```